Business cards and Stationary for Bright Learning Alliance
A Chinese Education Consulting Company
Business cards and Stationary for Bright Learning Alliance - Education
Creative Brief
Professional
Dennis R. Tolwy
Manager
7214 Marlow Court, San Ramon, CA 94583
dennistolwy@brilearnal.com
www.brilearnal.com
Please leave abundant space for multi address, (2) multi cell phones (3)

```html
<!DOCTYPE html>
<html lang="en">
<head>
<meta charset="utf-8">
<title>Bright Learning Alliance – Business Card</title>
<link rel="stylesheet" href="https://fonts.googleapis.com/css2?family=Open+Sans:ital,wght@0,400;0,600;0,700;1,700&display=swap">
<style>
  :root {
    --backdrop: #e9e6e2;
    --card: #ffffff;
    --red: #c8161d;
    --gold: #c9a24a;
    --ink: #4a4a4a;
  }
  * { margin: 0; padding: 0; box-sizing: border-box; }
  html, body {
    width: 1200px; height: 914px; overflow: hidden;
    background: var(--backdrop);
    font-family: "Open Sans", Arial, sans-serif;
  }
  .card {
    position: absolute; left: 50px; top: 142px;
    width: 1100px; height: 629px;
    background: var(--card);
    box-shadow: 0 6px 24px rgba(0,0,0,.18);
    overflow: hidden;
  }
  .swoosh { position: absolute; inset: 0; width: 1100px; height: 629px; }
  .brand {
    position: absolute; left: 78px; top: 120px;
    display: flex; align-items: center; gap: 14px;
  }
  .brand-dot { width: 30px; height: 30px; border-radius: 50%; background: var(--red); }
  .brand-name { font-size: 26px; font-weight: 700; color: var(--red); }
  .contacts {
    position: absolute; left: 78px; top: 262px;
    list-style: none; color: var(--ink); font-size: 21px; line-height: 31px;
  }
  .contacts li { display: flex; align-items: flex-start; gap: 12px; }
  .contacts .icon {
    flex: none; width: 22px; height: 22px; margin-top: 4px;
    border-radius: 50%; background: var(--red);
    display: flex; align-items: center; justify-content: center;
  }
  .contacts .icon svg { width: 12px; height: 12px; fill: #fff; }
  .contacts .no-icon { width: 22px; flex: none; }
  .person {
    position: absolute; right: 60px; top: 520px; text-align: right;
  }
  .person-name { font-size: 25px; font-weight: 700; font-style: italic; color: var(--red); }
  .person-role { font-size: 19px; color: var(--ink); margin-top: 2px; }
</style>
</head>
<body>
  <div class="card">
    <svg class="swoosh" viewBox="0 0 1100 629" aria-hidden="true">
      <defs>
        <linearGradient id="redFill" x1="0" y1="0" x2="1" y2="1">
          <stop offset="0" stop-color="#e02a2f"/>
          <stop offset="1" stop-color="#9c0d13"/>
        </linearGradient>
        <linearGradient id="goldFill" x1="0" y1="0" x2="1" y2="1">
          <stop offset="0" stop-color="#f3dd9a"/>
          <stop offset="1" stop-color="#b88a32"/>
        </linearGradient>
      </defs>
      <path d="M560,0 C790,30 980,80 1100,95" fill="none" stroke="url(#goldFill)" stroke-width="5"/>
      <path d="M660,40 C860,75 1010,120 1100,120 L1100,470 C1050,280 900,120 660,40 Z" fill="url(#redFill)"/>
      <path d="M630,55 C860,125 1030,280 1082,470" fill="none" stroke="url(#goldFill)" stroke-width="7"/>
    </svg>

    <div class="brand">
      <span class="brand-dot"></span>
      <span class="brand-name">Bright Learning Alliance</span>
    </div>

    <ul class="contacts">
      <li><span class="icon"><svg viewBox="0 0 12 12"><path d="M6 0a4 4 0 0 0-4 4c0 3 4 8 4 8s4-5 4-8a4 4 0 0 0-4-4zm0 5.5A1.5 1.5 0 1 1 6 2.5a1.5 1.5 0 0 1 0 3z"/></svg></span>7214 Marlow Court</li>
      <li><span class="no-icon"></span>San Ramon, CA 94583</li>
      <li><span class="icon"><svg viewBox="0 0 12 12"><path d="M2.5 0l2 2.5-1 1.5a7 7 0 0 0 4.5 4.5l1.5-1 2.5 2-1.5 2.5C5 12 0 7 0 1.5z"/></svg></span>+1 650-555-0142</li>
      <li><span class="icon"><svg viewBox="0 0 12 12"><rect x="3" y="0" width="6" height="12" rx="1.2"/></svg></span>+86-188-000-215-37</li>
      <li><span class="icon"><svg viewBox="0 0 12 12"><path d="M0 2h12v8H0zM1 3l5 4 5-4" stroke="#c8161d" stroke-width="0.8"/></svg></span>dennistolwy@brilearnal.com</li>
      <li><span class="icon"><svg viewBox="0 0 12 12"><circle cx="6" cy="6" r="5" fill="none" stroke="#fff" stroke-width="1.2"/><path d="M1 6h10M6 1v10" stroke="#fff" stroke-width="1"/></svg></span>www.brilearnal.com</li>
    </ul>

    <div class="person">
      <div class="person-name">Dennis R. Tolwy</div>
      <div class="person-role">Manager</div>
    </div>
  </div>
</body>
</html>
```